Personal Finance Blog Wordpress Design

We are looking for a new Wordpress theme design for CoinHarbor.com.

All of the elements that are currently on the homepage should remain, minus the archives list. The placement of various elements can be changed, we just need a more modern and clean feel. We would like to add a 160 x 600 ad unit on the homepage. We would like the 728x90 ad to be below the navigation similar to that of: http://www.plumtreeledger.example/blog/

We like the fonts used on: http://www.quillpocket.example/blog/

The text that currently resides at the bottom of CoinHarbor.com needs to remain on the homepage, but wherever it is placed needs to not be intrusive.

The color scheme needs to appropriately compliment the logo.

No sliders. I don't like sliders.

I am happy to answer questions.

Industry/Entity Type

Finance

Requirements
Must have
• Included in project description
Nice to have
Should not have
• Included in project description. Don't use sliders

```html
<!DOCTYPE html>
<html lang="en">
<head>
<meta charset="utf-8">
<title>Coin Harbor – Personal Finance Blog</title>
<link rel="stylesheet" href="https://fonts.googleapis.com/css2?family=Open+Sans:wght@400;600;700&family=Roboto+Slab:wght@400;700&display=swap">
<style>
:root{
  --green:#2d6a25;
  --green-dark:#245a1d;
  --lime:#8dc21f;
  --lime-soft:#9cc32a;
  --ink:#333333;
  --muted:#8a8a8a;
  --rule:#e2e2e2;
  --panel:#ececec;
  --meta:#e6e6e6;
  --footer:#2b2b2b;
  --footer-bar:#1f1f1f;
  --white:#ffffff;
  --sans:"Open Sans",Arial,sans-serif;
  --slab:"Roboto Slab",Georgia,serif;
}
*{box-sizing:border-box;margin:0;padding:0}
html,body{width:1200px;height:2691px;overflow:hidden;background:var(--white)}
body{position:relative;font-family:var(--sans);color:var(--ink)}
.abs{position:absolute}

/* header */
.brand{left:88px;top:34px;display:flex;align-items:center;gap:10px}
.brand-mark{width:30px;height:30px;background:var(--green);border-radius:50%}
.brand-name{font-family:var(--sans);font-weight:700;font-size:27px;color:var(--green);letter-spacing:-.3px}
.social-top{left:716px;top:39px;display:flex;gap:6px}
.social-top span{width:27px;height:27px;display:block;border-radius:2px}
.search{left:878px;top:40px;width:232px;height:30px;border:1px solid #cfcfcf;background:#f5f5f5;font-size:12px;color:#999;padding:6px 9px;display:flex;justify-content:space-between;align-items:center}

/* nav */
.main-nav{left:88px;top:106px;width:1024px;height:41px;background:var(--green);display:flex;align-items:center}
.main-nav a{color:var(--white);text-decoration:none;font-size:14.5px;padding:0 15px;height:41px;line-height:41px}
.main-nav a.active{background:var(--lime);padding:0 18px}
.main-nav a:last-child{margin-left:auto}

/* leaderboard */
.leaderboard{left:235px;top:178px;width:728px;height:90px;display:flex;overflow:hidden}
.lb-photo{width:218px;background:linear-gradient(135deg,#c9d7e3,#8ca3b8)}
.lb-copy{flex:1;background:#2aa6d8;position:relative}
.lb-head{position:absolute;left:0;top:0;right:0;height:32px;background:#8b1a3c;color:#fff;font-weight:700;font-size:20px;line-height:32px;padding-left:14px;white-space:nowrap}
.lb-head b{color:#ffdf5c}
.lb-badge{position:absolute;left:8px;top:38px;width:46px;height:46px;border-radius:50%;background:#e6eef6}
.lb-list{position:absolute;left:64px;top:38px;color:#fff;font-size:11px;line-height:15px;list-style:none;white-space:nowrap}
.lb-cta{position:absolute;right:16px;top:40px;color:#fff;font-weight:700;font-size:17px;line-height:20px;text-align:right;white-space:nowrap}

/* feature grid */
.feature{overflow:hidden}
.feature .fill{position:absolute;inset:0}
.feature-lead{left:88px;top:300px;width:371px;height:432px}
.lead-text{position:absolute;left:16px;right:16px;top:140px;display:flex;flex-direction:column;align-items:center;gap:14px}
.lead-title{text-align:center;color:#fff;font-family:var(--slab);font-weight:700;font-size:23px;line-height:30px;text-transform:uppercase;white-space:nowrap}
.lead-date{text-align:center;color:#fff;font-style:italic;font-size:14px}
.feature-tile{width:316px;height:214px}
.tile-cap{position:absolute;left:0;right:0;bottom:0;height:57px;color:#fff;text-align:center;font-size:14px;padding-top:9px;line-height:20px}
.tile-cap i{display:block;font-size:12.5px}
.cap-dark{background:var(--green)}
.cap-lime{background:var(--lime-soft)}

/* section tab headings */
.tab-head{height:38px;border-bottom:3px solid var(--green)}
.tab-head span{display:inline-block;height:35px;line-height:35px;background:var(--green);color:#fff;font-family:var(--slab);font-size:17px;padding:0 14px}

/* post cards */
.card-img{position:absolute;left:0;right:0}
.card-meta{position:absolute;left:0;right:0;height:34px;background:var(--meta);color:var(--muted);font-size:13px;line-height:34px;padding:0 12px;display:flex;justify-content:space-between;align-items:center}
.card-meta em{font-style:normal;display:flex;align-items:center;gap:4px}
.card-title{position:absolute;left:0;right:0;font-size:17px;line-height:23px;color:#222}
.card-excerpt{position:absolute;left:0;right:0;font-size:13.5px;line-height:20px;color:var(--muted)}

/* blog intro */
.intro-text{left:434px;top:1298px;width:340px;font-size:13.5px;line-height:20.5px;color:var(--muted)}

/* sidebar tabs */
.side-tabs{left:797px;top:771px;width:315px;height:445px;background:var(--panel)}
.side-tabs nav{display:flex;height:40px;background:#fff}
.side-tabs nav span{flex:1;text-align:center;line-height:40px;font-family:var(--slab);font-size:14px;color:#444}
.side-tabs nav span.on{background:var(--panel);color:var(--lime);border-top:3px solid var(--lime);line-height:36px}
.pop-list{list-style:none;padding:6px 14px}
.pop-list li{display:flex;gap:10px;height:75px;padding-top:8px;border-bottom:1px solid #d8d8d8;overflow:hidden}
.pop-list li:last-child{border-bottom:0}
.pop-thumb{width:64px;height:58px;flex:none}
.pop-body{flex:1;position:relative}
.pop-date{font-size:11px;color:var(--green)}
.pop-count{position:absolute;right:0;top:0;font-size:11px;color:#999}
.pop-title{font-size:11px;line-height:16px;color:#333;margin-top:6px}

/* newsletter */
.news{left:797px;top:1247px;width:315px}
.news p{font-size:13.5px;line-height:20px;color:#333;margin-top:14px}
.news form{display:flex;margin-top:12px}
.news .field{flex:1;height:41px;background:#eaeaea;font-size:11.5px;font-style:italic;color:#888;line-height:41px;padding-left:12px}
.news .send{width:70px;height:41px;background:var(--green);color:#fff;font-size:16px;text-align:center;line-height:41px}
.connect{left:797px;top:1417px;width:315px;height:129px;background:var(--panel);padding:14px 22px}
.connect h3{font-family:var(--slab);font-weight:400;font-size:15px;color:#444}
.connect ul{list-style:none;display:flex;gap:26px;margin-top:12px}
.connect li{text-align:center;font-size:12px;color:#333;width:46px}
.connect li span{display:block;width:44px;height:44px;margin:0 auto 6px}

/* skyscraper */
.skyscraper{left:872px;top:1623px;width:160px;height:600px;background:#0f2a4d;color:#fff;overflow:hidden}
.sky-head{padding:14px 10px 0;font-weight:700;font-size:22px;line-height:25px;letter-spacing:-.4px;white-space:nowrap}
.sky-copy{padding:8px 10px 0;font-size:10px;line-height:13px;color:#dfe8f4}
.sky-art{position:absolute;left:0;right:0;top:195px;height:240px;background:radial-gradient(circle at 55% 40%,#9fd6ff,#2f6fb0 45%,#0f2a4d 80%)}
.sky-foot{position:absolute;left:0;right:0;top:455px;height:145px;background:#fff;color:#123}
.sky-sq{position:absolute;left:10px;top:14px;width:26px;height:26px;background:#2d8fbf;border-radius:50%}
.sky-name{position:absolute;left:44px;top:12px;font-size:10.5px;font-weight:700;line-height:12px;color:#2d6ea8}
.sky-tag{position:absolute;left:44px;top:52px;font-size:8px;color:#777}
.sky-btn{position:absolute;left:0;right:0;bottom:0;height:62px;background:#111;color:#fff;text-align:center;font-size:12px;line-height:15px;padding-top:17px;font-weight:600}

/* footer */
.site-footer{left:0;top:2368px;width:1200px;height:283px;background:var(--footer);color:#fff}
.foot-col{position:absolute;top:40px}
.foot-col h4{font-family:var(--slab);font-weight:400;font-size:19px;display:flex;align-items:center;gap:10px;border-bottom:1px solid #555;padding-bottom:9px}
.foot-col p{font-size:12.5px;line-height:19.5px;margin-top:12px}
.foot-col ul{list-style:none;margin-top:10px}
.foot-col li{font-size:12.5px;line-height:17px;margin-bottom:7px;position:relative;padding-left:14px}
.foot-col li::before{content:"";position:absolute;left:0;top:7px;width:5px;height:1px;background:#aaa}
.sitemap li{margin-bottom:6px}
.foot-bar{left:0;top:2651px;width:1200px;height:40px;background:var(--footer-bar);color:#ddd;font-size:12px;line-height:40px}
.foot-bar .left{position:absolute;left:88px}
.foot-bar .right{position:absolute;right:88px}
</style>
</head>
<body>

<header>
  <div class="abs brand"><span class="brand-mark"></span><span class="brand-name">CoinHarbor</span></div>
  <div class="abs social-top">
    <span style="background:#2aa3df"></span><span style="background:#2d5ba5"></span><span style="background:#d6392a"></span><span style="background:#e8912c"></span>
  </div>
  <div class="abs search">Search...
    <svg width="12" height="12" viewBox="0 0 12 12"><circle cx="5" cy="5" r="3.6" fill="none" stroke="#aaa" stroke-width="1.4"/><path d="M7.6 7.6L11 11" stroke="#aaa" stroke-width="1.4"/></svg>
  </div>
</header>

<nav class="abs main-nav">
  <a class="active">Auto</a><a>Bank Accounts</a><a>Credit Cards</a><a>Insurance</a><a>Investments</a><a>Mortgages</a><a>Personal Finance</a><a>Small Business</a><a>Taxes</a>
</nav>

<aside class="abs leaderboard" aria-label="Advertisement">
  <div class="lb-photo" role="img" aria-label="Family standing beside a new car at a dealership"></div>
  <div class="lb-copy">
    <div class="lb-head">It's the <b>Best</b> Time in Years to Buy a Car</div>
    <span class="lb-badge"></span>
    <ul class="lb-list"><li>• Great deals and incentives</li><li>• Credit is available</li><li>• Highest quality and fuel efficiency</li></ul>
    <div class="lb-cta">Visit your local new-car<br>dealership today.</div>
  </div>
</aside>

<section aria-label="Featured posts">
  <article class="abs feature feature-lead">
    <div class="fill" role="img" aria-label="Person holding a piggy bank" style="background:linear-gradient(160deg,#6b5446,#2c2522 60%,#4a3a33)"></div>
    <div class="lead-text">
      <h2 class="lead-title">Save more money<br>shopping online<br>using your Marketbay<br>Plus benefits</h2>
      <div class="lead-date">May 1st, 2015</div>
    </div>
  </article>
  <article class="abs feature feature-tile" style="left:470px;top:300px">
    <div class="fill" role="img" aria-label="Children with backpacks boarding a school bus" style="background:linear-gradient(135deg,#e0b640,#8a8f7a 55%,#566a3c)"></div>
    <div class="tile-cap cap-dark">Going back to School<i>May 1st, 2015</i></div>
  </article>
  <article class="abs feature feature-tile" style="left:796px;top:300px">
    <div class="fill" role="img" aria-label="Hand holding a credit card" style="background:linear-gradient(135deg,#d9d4cf,#a0938a 60%,#6e5f58)"></div>
    <div class="tile-cap cap-lime">First time Credit Card Holders<i>May 1st, 2015</i></div>
  </article>
  <article class="abs feature feature-tile" style="left:470px;top:518px">
    <div class="fill" role="img" aria-label="Modern living room with sofa and pendant lamps" style="background:linear-gradient(180deg,#c9c9c6,#efefec 55%,#d8d8d4)"></div>
    <div class="tile-cap cap-lime">Why Buy Furniture Online?<i>May 1st, 2015</i></div>
  </article>
  <article class="abs feature feature-tile" style="left:796px;top:518px">
    <div class="fill" role="img" aria-label="Calculator on a mortgage application form" style="background:linear-gradient(135deg,#7c7c7c,#cfcfcf 55%,#a58e74)"></div>
    <div class="tile-cap cap-dark">Loan Interest Rates for 2015?<i>May 1st, 2015</i></div>
  </article>
</section>

<section class="abs" style="left:88px;top:771px;width:326px;height:440px">
  <div class="tab-head"><span>Orbitone Radio Stock</span></div>
  <div class="card-img" role="img" aria-label="Businessman drawing a rising arrow chart" style="top:58px;height:206px;background:linear-gradient(135deg,#f2f2f2,#c9c9c9 60%,#3b4250)"></div>
  <div class="card-meta" style="top:264px"><span>Apr 29th, 2015</span><em>▭ 0</em></div>
  <h3 class="card-title" style="top:318px;font-weight:400">Orbitone Radio Stock: How Fares in 2015</h3>
  <p class="card-excerpt" style="top:348px">As the days of satellite radio seem to be numbered, there seems to be more interest on the shares of industry leader Orbitone than on the company itself..</p>
</section>
<section class="abs" style="left:452px;top:771px;width:320px;height:440px">
  <div class="tab-head"><span>Auto</span></div>
  <div class="card-img" role="img" aria-label="Dealer handing car keys to a customer" style="top:58px;height:206px;background:linear-gradient(135deg,#d4d8dc,#9aa3ab 55%,#4c4a4a)"></div>
  <div class="card-meta" style="top:264px"><span>Apr 29th, 2015</span><em>▭ 0</em></div>
  <h3 class="card-title" style="top:318px;font-weight:400">Benefits of a Lumen Rewards Card</h3>
  <p class="card-excerpt" style="top:348px">Credit cards open a new world of opportunities and allow consumers to build up their credit scores. Unfortunately, they also cost most people a lot of money over time. If you've just gotten your first credit card,</p>
</section>

<aside class="abs side-tabs">
  <nav><span class="on">POPULAR</span><span>RECENT</span><span>LATEST</span></nav>
  <ul class="pop-list">
    <li><div class="pop-thumb" role="img" aria-label="Mortgage paperwork" style="background:linear-gradient(135deg,#bbb,#666)"></div><div class="pop-body"><div class="pop-date">Apr 29th, 2015</div><span class="pop-count">▭ 4</span><div class="pop-title">How Do Home Loan Interest Rates Look For 2015?</div></div></li>
    <li><div class="pop-thumb" role="img" aria-label="Colourful school supplies" style="background:linear-gradient(135deg,#e7b84a,#6aa0c8)"></div><div class="pop-body"><div class="pop-date">Apr 29th, 2015</div><span class="pop-count">▭ 4</span><div class="pop-title">Going Back to School? Five Benefits of Tuition Reimbursement</div></div></li>
    <li><div class="pop-thumb" role="img" aria-label="Car keys on paperwork" style="background:linear-gradient(135deg,#ddd,#555)"></div><div class="pop-body"><div class="pop-date">Apr 29th, 2015</div><span class="pop-count">▭ 4</span><div class="pop-title">Car Shopping on a Budget? Warecrest Car Buying Is a Great Option</div></div></li>
    <li><div class="pop-thumb" role="img" aria-label="Furnished living room" style="background:linear-gradient(135deg,#c8b28f,#6d5a43)"></div><div class="pop-body"><div class="pop-date">Apr 29th, 2015</div><span class="pop-count">▭ 4</span><div class="pop-title">Why You Should Buy Furniture Online</div></div></li>
    <li><div class="pop-thumb" role="img" aria-label="Furnished living room" style="background:linear-gradient(135deg,#bfbfbf,#5a5a5a)"></div><div class="pop-body"><div class="pop-date">Apr 29th, 2015</div><span class="pop-count">▭ 4</span><div class="pop-title">Why You Should Buy Furniture Online</div></div></li>
  </ul>
</aside>

<section class="abs" style="left:88px;top:1240px;width:684px">
  <div class="tab-head"><span>Coin Harbor: Personal Finance Blog</span></div>
</section>
<div class="abs" role="img" aria-label="Desk with laptop, notebook and pens" style="left:88px;top:1304px;width:335px;height:158px;background:linear-gradient(135deg,#cfc4b0,#8c8a86 50%,#3d4756)"></div>
<p class="abs intro-text">Our mission is to enrich the lives of our readers (literally!) by providing the very best personal finance content on the internet. Our readers may be at different stages in life, with different personal finance situations and needs: One person may be looking to get their first credit card, another might be looking into how to get a mortgage to buy a home, some may be looking for ways to afford or finance a college</p>

<aside class="abs news">
  <div class="tab-head"><span style="font-size:15.5px">SIGN UP FOR NEWSLETTER</span></div>
  <p>Sign up now to receive breaking news and to hear what's new with our website!</p>
  <form><div class="field">Enter your Email address</div><div class="send">Send</div></form>
</aside>
<aside class="abs connect">
  <h3>CONNECT WITH US</h3>
  <ul>
    <li><span style="background:#2aa3df"></span>Chirper</li>
    <li><span style="background:#2d5ba5"></span>Friendbook</li>
    <li><span style="background:#d6392a"></span>CirclePlus</li>
    <li><span style="background:#e8912c"></span>RSS</li>
  </ul>
</aside>

<aside class="abs skyscraper" aria-label="Advertisement">
  <div class="sky-head">MAKE YOUR<br>BUSINESS<br>SMARTER.</div>
  <div class="sky-copy">Greenridge's newest resource helps you build a workforce that's well-trained and adaptable to your changing needs.</div>
  <div class="sky-art" role="img" aria-label="Hand touching a glowing interface"></div>
  <div class="sky-foot">
    <span class="sky-sq"></span>
    <div class="sky-name">GREENRIDGE<br>CORPORATE<br>COLLEGE</div>
    <div class="sky-tag">building smarter teams</div>
    <div class="sky-btn">CLICK TO<br>LEARN MORE</div>
  </div>
</aside>

<section class="abs" style="left:88px;top:1507px;width:337px;height:420px">
  <div class="tab-head"><span style="font-size:15.5px">Bank Accounts</span></div>
  <div class="card-img" role="img" aria-label="Seedling growing from a jar of coins" style="top:57px;height:172px;background:linear-gradient(135deg,#e5d9a8,#9b8c5e 55%,#5d6b3a)"></div>
  <div class="card-meta" style="top:229px"><span>Apr 29th, 2015</span><em>▭ 0</em></div>
  <h3 class="card-title" style="top:280px;font-weight:400;font-size:16px">Want to Increase Your Savings? Check Out These Great Saving Money Tips</h3>
  <p class="card-excerpt" style="top:328px">Increasing the amount of money in a savings account is a goal shared by many people all over the country. In the United States, the national savings rate...</p>
</section>
<section class="abs" style="left:436px;top:1507px;width:335px;height:420px">
  <div class="tab-head"><span style="font-size:15.5px">Dental</span></div>
  <div class="card-img" role="img" aria-label="Child in a dentist chair" style="top:57px;height:172px;background:linear-gradient(135deg,#bfe3ea,#7fb8c9 55%,#d8c0b2)"></div>
  <div class="card-meta" style="top:229px"><span>Apr 29th, 2015</span><em>▭ 0</em></div>
  <h3 class="card-title" style="top:280px;font-weight:400;font-size:16px">Car Shopping on a Budget? Warecrest Car Buying Is a Great Option</h3>
  <p class="card-excerpt" style="top:328px">Many consumers are currently searching for a reliable new or used vehicle, and want to make sure they get the best deal. Some people need a vehicle so...</p>
</section>

<section class="abs" style="left:88px;top:1946px;width:337px;height:380px">
  <div class="tab-head"><span style="font-size:15.5px">Bank Accounts</span></div>
  <div class="card-img" role="img" aria-label="Woman holding a blue piggy bank" style="top:58px;height:170px;background:linear-gradient(135deg,#c98a55,#8a4a2c 55%,#5a86b5)"></div>
  <div class="card-meta" style="top:228px"><span>Apr 29th, 2015</span><em>▭ 0</em></div>
  <h3 class="card-title" style="top:279px;font-weight:400;font-size:16px">Want to Increase Your Savings? Check Out These Great Saving Money Tips</h3>
  <p class="card-excerpt" style="top:327px">Increasing the amount of money in a savings account is a goal shared by...</p>
</section>
<section class="abs" style="left:436px;top:1946px;width:335px;height:380px">
  <div class="tab-head"><span style="font-size:15.5px">Auto</span></div>
  <div class="card-img" role="img" aria-label="Approved car loan form with car keys" style="top:58px;height:170px;background:linear-gradient(135deg,#f0f0f0,#b8b8b8 60%,#6a6a6a)"></div>
  <div class="card-meta" style="top:228px"><span>Apr 29th, 2015</span><em>▭ 0</em></div>
  <h3 class="card-title" style="top:279px;font-weight:400;font-size:16px">Car Shopping on a Budget? Warecrest Car Buying Is a Great Option</h3>
  <p class="card-excerpt" style="top:327px">Many consumers are currently searching for a reliable new or used vehicle...</p>
</section>

<footer class="abs site-footer">
  <div class="foot-col" style="left:88px;width:310px">
    <h4><svg width="20" height="20" viewBox="0 0 20 20"><circle cx="10" cy="10" r="8.5" fill="none" stroke="#fff" stroke-width="1.8"/><path d="M7.3 7.8a2.7 2.7 0 1 1 3.6 2.5c-.7.3-.9.8-.9 1.6" fill="none" stroke="#fff" stroke-width="1.8"/><circle cx="10" cy="14.6" r="1.1" fill="#fff"/></svg>About Coin Harbor</h4>
    <p>Our mission is to enrich the lives of our readers (literally!) by providing the very best personal finance content on the internet. Our readers may be at different stages in life, with different personal finance situations and needs: One person may be looking to get their first credit card, another might be looking into how to get.One person may be looking to get their first credit card, another.</p>
  </div>
  <div class="foot-col" style="left:481px;width:326px">
    <h4><svg width="20" height="20" viewBox="0 0 20 20"><circle cx="10" cy="10" r="8.5" fill="none" stroke="#fff" stroke-width="1.8"/><path d="M10 5v5l3.2 2" fill="none" stroke="#fff" stroke-width="1.8"/></svg>From The Blog</h4>
    <ul>
      <li>How Do Home Loan Interest Rates Look For 2015?</li>
      <li>Going Back to School? Five Benefits of Tuition Reimbursement</li>
      <li>Car Shopping on a Budget? Warecrest Car Buying Is a Great Option</li>
      <li>Why You Should Buy Furniture Online</li>
      <li>Best Budgeting Software for 2015</li>
    </ul>
  </div>
  <div class="foot-col sitemap" style="left:911px;width:201px">
    <h4><svg width="18" height="20" viewBox="0 0 18 20"><path d="M2 1h9l5 5v13H2z" fill="#fff"/><path d="M5 10h8M5 13h8M5 16h6" stroke="#2b2b2b" stroke-width="1.4"/></svg>Sitemap</h4>
    <ul>
      <li>Auto</li><li>Bank Accounts</li><li>Credit Cards</li><li>Insurance</li><li>Investments</li><li>Mortgages</li><li>Personal Finance</li><li>Small Business</li>
    </ul>
  </div>
</footer>
<div class="abs foot-bar"><span class="left">© 2015 Coin Harbor. All rights reserved</span><span class="right">Privacy Policy | Terms and Conditions</span></div>

</body>
</html>
```